New company cut sheet “one page” description of services (double sided) *

Harrowgate Ridge Partners, LLC is looking for a newly designed one page sheet that describes the companies services. We will provide our logo and some images and content.

Target Market(s)

Companies that need to raise money or real estate owners that are looking to finance or re-finance. Raising debt and equity financing for companies looking to raise 2MM to 100MM

Industry/Entity Type

Real Estate Development

Font styles to use
Serif
Decorative

Colors

Designer to choose colors to be used in the design.

Requirements
Must have
• Logo, website, company description, why we are better. We would like some possible graphics that are regal and classy. Please list that our offices are located on Linden Row in New York, Philadelphia, Houston and Austin
Nice to have
• Good graphics that gives the impression we are very high class and professional. Maybe a skyline or office buildings. Classy and elegant. High end business class. We are raising money for indivual projects and companies from 2MM to 100MM

```html
<!DOCTYPE html>
<html lang="en">
<head>
<meta charset="utf-8">
<title>Harrowgate Ridge Partners – Services Sheet</title>
<link href="https://fonts.googleapis.com/css2?family=Tinos:wght@400;700&display=swap" rel="stylesheet">
<style>
  :root {
    --navy: #0c0a4f;
    --white: #ffffff;
    --mist: #dcdee2;
    --mist-light: #eceef0;
    --ground: #e6e7ea;
    --ink-body: #2a2a3a;
    --steel-dark: #3d4249;
    --steel-light: #c9ced4;
    --sky-deep: #2d6fd6;
    --sky-light: #8fd6f0;
  }
  * { box-sizing: border-box; margin: 0; padding: 0; }
  html, body { width: 1200px; height: 822px; overflow: hidden; }
  body {
    background: var(--ground);
    font-family: "Tinos", "Times New Roman", serif;
    position: relative;
  }
  .sheet {
    position: absolute;
    top: 41px;
    width: 572px;
    height: 740px;
    background: var(--white);
    overflow: hidden;
    box-shadow: 0 6px 18px rgba(0,0,0,.18);
  }
  .sheet--front { left: 18px; }
  .sheet--back { left: 610px; }
  .sheet-art { position: absolute; inset: 0; width: 572px; height: 740px; }

  /* Front */
  .brand {
    position: absolute; top: 62px; left: 250px; width: 300px;
    display: flex; align-items: center; gap: 10px; justify-content: center;
  }
  .brand-mark { width: 22px; height: 22px; background: var(--navy); flex: none; }
  .brand-name {
    color: var(--navy); font-size: 17px; font-weight: 400;
    letter-spacing: .06em; text-transform: uppercase; white-space: nowrap;
  }
  .intro {
    position: absolute; top: 140px; left: 205px; width: 335px;
    font-size: 9.6px; line-height: 1.42; color: var(--ink-body);
  }
  .intro p + p { margin-top: 10px; text-indent: 20px; }
  .slogan {
    position: absolute; top: 432px; right: 24px;
    color: var(--navy); font-size: 26px; font-weight: 700; line-height: 1.05;
    text-align: right; text-transform: uppercase; letter-spacing: .02em;
  }
  .services {
    position: absolute; top: 508px; left: 36px; width: 320px;
    color: var(--white); font-size: 9px; line-height: 1.38;
  }
  .services p + p { margin-top: 9px; }
  .website {
    position: absolute; bottom: 22px; right: 24px;
    color: var(--white); font-size: 20px; font-weight: 700; letter-spacing: .05em;
  }

  /* Back */
  .advantages-title {
    position: absolute; top: 30px; left: 30px;
    color: var(--navy); font-size: 20px; line-height: 1.15;
    text-transform: uppercase; letter-spacing: .06em;
  }
  .point {
    position: absolute; display: flex; align-items: flex-start; gap: 10px;
    font-size: 10.5px; line-height: 1.38;
  }
  .point-numeral { font-size: 32px; line-height: .9; flex: none; }
  .point--light { color: var(--navy); }
  .point--dark { color: var(--white); }
  .point--i   { top: 140px; left: 30px;  width: 420px; }
  .point--ii  { top: 198px; left: 30px;  width: 480px; }
  .point--iii { top: 256px; left: 30px;  width: 430px; }
  .point--iv  { top: 330px; left: 416px; width: 152px; }
  .point--v   { top: 444px; left: 318px; width: 240px; }
  .point--vi  { top: 510px; left: 218px; width: 340px; }
  .point--vii { top: 592px; left: 104px; width: 450px; }
  .contact-title {
    position: absolute; top: 420px; left: 30px; width: 170px;
    color: var(--navy); font-size: 26px; font-weight: 700; line-height: 1.05;
    text-align: center; text-transform: uppercase; letter-spacing: .03em;
  }
  .email {
    position: absolute; top: 680px; left: 40px;
    color: var(--white); font-size: 20px; letter-spacing: .05em;
  }
</style>
</head>
<body>

<section class="sheet sheet--front">
  <svg class="sheet-art" viewBox="0 0 572 740">
    <defs>
      <linearGradient id="steel" x1="0" y1="0" x2="1" y2="1">
        <stop offset="0" stop-color="#3d4249"/>
        <stop offset=".55" stop-color="#c9ced4"/>
        <stop offset="1" stop-color="#eef0f2"/>
      </linearGradient>
    </defs>
    <polygon role="img" aria-label="Photograph of office towers seen from below"
      points="0,0 572,0 572,28 230,28 110,340 0,360" fill="url(#steel)"/>
    <polygon points="572,170 572,600 250,545" fill="#dcdee2"/>
    <polygon points="0,330 572,600 572,740 0,740" fill="#0c0a4f"/>
    <polygon points="0,690 150,740 0,740" fill="#eceef0"/>
  </svg>

  <div class="brand">
    <span class="brand-mark"></span>
    <span class="brand-name">Harrowgate Ridge Partners</span>
  </div>

  <div class="intro">
    <p>Harrowgate Ridge Partners, LLC (HRP) is a boutique commercial mortgage-banking firm with a regional focus and national capabilities. HRP leverages an extensive network of traditional and nontraditional capital for your commercial real estate transactions locally and globally.</p>
    <p>We maintain a narrow focus on placing debt and equity for income producing, owner-occupied, land development, and “for-sale” real estate transactions. We pride ourselves on being able to execute both common and relatively complex transactions with equal effectiveness.</p>
  </div>

  <h2 class="slogan">Grow your<br>business</h2>

  <div class="services">
    <p>HRP offers a variety of loan types tailored to suit any commercial real estate requirement, including permanent loans for refinance and acquisition, construction loans, bridge loans, mezzanine/preferred equity, and traditional equity.</p>
    <p>Harrowgate Ridge Partners’ mission is to protect the best interest of our clients and to meet their specific needs. Through our unique process accessing traditional and nontraditional capital sources, we provide the very best debt and equity solutions tailored to ensure success.</p>
    <p>We feel a keen responsibility to provide our clients with services far above and beyond those they experienced with traditional real estate business models.</p>
    <p>Our years of commercial banking and finance experience arranging large-scale commercial debt and equity financing raises the level of excellence we bring to each partnership.</p>
  </div>

  <div class="website">WWW.COMPANY.COM</div>
</section>

<section class="sheet sheet--back">
  <svg class="sheet-art" viewBox="0 0 572 740">
    <defs>
      <linearGradient id="sky" x1="0" y1="0" x2="1" y2="1">
        <stop offset="0" stop-color="#8fd6f0"/>
        <stop offset="1" stop-color="#2d6fd6"/>
      </linearGradient>
    </defs>
    <polygon role="img" aria-label="Blue financial growth chart graphic"
      points="300,0 572,0 572,170 480,170" fill="url(#sky)"/>
    <polygon points="0,360 330,360 0,660" fill="#dcdee2"/>
    <polygon points="572,200 572,600 470,740 0,740 0,660" fill="#0c0a4f"/>
  </svg>

  <h2 class="advantages-title">Why we are<br>better<br>than our<br>competitors</h2>

  <div class="point point--light point--i"><span class="point-numeral">I</span><span>We are experienced former commercial bankers who understand where and how to source the very best financing arrangements for our clients.</span></div>
  <div class="point point--light point--ii"><span class="point-numeral">II</span><span>Our vast network of correspondent lenders offers regional and national experience.</span></div>
  <div class="point point--light point--iii"><span class="point-numeral">III</span><span>We are commercial property owners ourselves and we treat every opportunity as if it was our own.</span></div>

  <h2 class="contact-title">Contact<br>us</h2>

  <div class="point point--dark point--iv"><span class="point-numeral">IV</span><span>Our processes are streamlined to meet all clients’ unique needs quickly and to get their projects moving forward as fast as possible.</span></div>
  <div class="point point--dark point--v"><span class="point-numeral">V</span><span>To ensure best service to our clients with no conflicts of interest, debt and equity solutions are all that we do.</span></div>
  <div class="point point--dark point--vi"><span class="point-numeral">VI</span><span>Because we understand the vital need for privacy and data security in today’s world of cyber threats, we have created our own proprietary system to ensure all data is protected.</span></div>
  <div class="point point--dark point--vii"><span class="point-numeral">VII</span><span>Our exclusive access to high-end lenders and off-market real estate gives us first shot at offering before-market incredible real estate opportunities to our private investors.</span></div>

  <div class="email">CONTACT@MAIL.COM</div>
</section>

</body>
</html>
```